Banner ad design for Vantora Display Ads

We are looking for a designer to develop a concept for banner ads for a Vantora Display campaign we are building.

We have 3 business lines, shredding services, records management services and scanning services.

We are looking for 4 sets of ads to be created, one for each business line + one set that showcases all of our lines together.

For the design concepts, we would like to see a few sizes (banner, square, leaderboard, skyscraper, etc) for each.

The person chosen will then need to create the ads into all Vantora supported sizes -- 20 sizes total for each set of ads as per the Vantora size guidelines found on this page - https://help.vantora-example.com/vantora-ads/answer/4827150?hl=en&ref_topic=6604821#

A few items to note:
- Design should complement our existing brand/website look and feel (www.oak-ferry.ca)
- Each final ad must be 150Kb or less in size
- Final designs should be editable, meaning if we would like to change some copy in the design, we can do so using a well-known software (Canva, Photoshop/InDesign, etc)
- Some images are attached for use, but if you feel a different stock image is more suitable to to your design, please go ahead and use it.

Provided below is some messaging that can be used for each set of ads. Do not feel you need to use all of the messaging, it is provided for guidance.

SHREDDING SERVICES:

Possible Short Headline:
-- One-Time Shredding Services
-- Secure Shredding Services
-- Affordable On-Site Shredding

Possible Long Headline
-- Your Paper Can be Destroyed as Soon as the Next Business Day

Possible Descriptions:
-- KVEC Gold Certified On site shredding company. Service as soon as Next Day.
-- Secure and Affordable Toronto & GTA On-Site Shredding.
-- Certified, Affordable Office Shredding Since 2003.
-- Quick, no contact and affordable paper shredding services in Toronto & Southern Ontario.
-- Certified, Affordable Office Shredding Since 2003. Fast, no contact shredding service.

Call to Action
-- Get a Quote

RECORDS MANAGEMENT
Short Headline:
-- Off-site Records Storage
-- Records Management & Storage
-- Secure Records Storage
-- Records Management Services
-- Long Term Records Management
-- Document Storage Solutions

Possible Description
-- Local, Affordable Storage Solutions. Protect and Store your Documents in our Secure Facility
-- Local, Affordable Records Management Solutions. Store your Records in our Secure Facility
-- Certified, Affordable Document Storage Since 2004. Contact Us for a Free Quote!
-- Vaultline+ Certified, Affordable Document Storage Since 2004. Contact Us for a Free Quote!

Call to Action
-- Get a Quote

SCANNING SERVICES

Short Headline:
-- Professional Scanning Company
-- Toronto & GTA Scanning Service
-- Document Scanning Services
-- Digital Conversion Services
-- Fast & Easy Retrieval

Description
-- Scan and documents and files with Professional scanning services from Oak-Ferry
-- Convert Your Paper Files to Electronic Files. Fast & Easy Retrieval.
-- Easily access your documents electronically with Document Scanning Services

Call to Action
-- Get a Quote

ALL SERVICES AD SET
Short Headline
-- Shred, Scan & Store Documents
-- Secure Shredding, Records Management and Scanning Services
-- #1 Document Management Company
-- Oak Ferry Shredding, Storage & Scanning

Description
-- Secure and Affordable Toronto & GTA On-Site Shredding, Document Storage & Scanning Company

Call to Action
-- Get a Quote

Font styles to use
Sans Serif

```html
<!DOCTYPE html>
<html lang="en">
<head>
<meta charset="utf-8">
<title>Oak Ferry Shredding Display Ads</title>
<link href="https://fonts.googleapis.com/css2?family=Montserrat:wght@400;500;600;700;800&display=swap" rel="stylesheet">
<style>
  :root {
    --board: #e6e6e6;
    --brand-blue: #1f69a6;
    --cta-orange: #f8a01d;
    --white: #ffffff;
    --ink: #1d2a36;
    --photo-light: #f6f2ec;
    --photo-mid: #e4cdb6;
    --photo-warm: #c99570;
  }
  * { margin: 0; padding: 0; box-sizing: border-box; }
  html, body { width: 1200px; height: 1135px; overflow: hidden; }
  body {
    background: var(--board);
    font-family: "Montserrat", Arial, sans-serif;
    position: relative;
  }
  .ad {
    position: absolute;
    background: var(--white);
    overflow: hidden;
  }
  .ad-art { position: absolute; inset: 0; width: 100%; height: 100%; }
  .ad-leaderboard { left: 91px; top: 68px; width: 1037px; height: 129px; }
  .ad-medium { left: 89px; top: 240px; width: 429px; height: 357px; }
  .ad-large { left: 89px; top: 697px; width: 481px; height: 400px; }
  .ad-skyscraper { left: 697px; top: 240px; width: 430px; height: 857px; }

  .brand-name {
    position: absolute;
    font-weight: 600;
    color: var(--ink);
    line-height: 1;
    white-space: nowrap;
  }

  .copy { position: absolute; color: var(--white); }
  .headline { font-weight: 800; line-height: 1.18; }
  .description { font-weight: 500; }
  .cta {
    position: absolute;
    background: var(--cta-orange);
    color: var(--white);
    font-weight: 700;
    border-radius: 4px;
    display: flex; align-items: center; justify-content: center;
    box-shadow: 0 3px 6px rgba(0,0,0,0.18);
  }

  /* leaderboard */
  .ad-leaderboard .brand-name { left: 8px; top: 14px; font-size: 9px; }
  .ad-leaderboard .copy { left: 78px; top: 28px; }
  .ad-leaderboard .headline { font-size: 22px; margin-bottom: 7px; }
  .ad-leaderboard .description { font-size: 13px; line-height: 1.4; }
  .ad-leaderboard .cta { left: 459px; top: 40px; width: 199px; height: 49px; font-size: 16px; }

  /* medium */
  .ad-medium .brand-name { left: 11px; top: 28px; font-size: 13px; }
  .ad-medium .copy { left: 22px; top: 184px; }
  .ad-medium .headline { font-size: 20px; margin-bottom: 7px; }
  .ad-medium .description { font-size: 11.5px; line-height: 1.5; }
  .ad-medium .cta { left: 22px; top: 290px; width: 185px; height: 42px; font-size: 13.5px; }

  /* large */
  .ad-large .brand-name { left: 17px; top: 28px; font-size: 15px; }
  .ad-large .copy { left: 28px; top: 226px; }
  .ad-large .headline { font-size: 23px; margin-bottom: 9px; }
  .ad-large .description { font-size: 14.3px; line-height: 1.4; }
  .ad-large .cta { left: 28px; top: 344px; width: 128px; height: 33px; font-size: 11.5px; }

  /* skyscraper */
  .ad-skyscraper .brand-name { left: 17px; top: 34px; font-size: 16px; }
  .ad-skyscraper .copy { left: 43px; top: 508px; width: 330px; }
  .ad-skyscraper .headline { font-size: 32px; margin-bottom: 18px; }
  .ad-skyscraper .description { font-size: 22px; line-height: 1.36; font-weight: 400; }
  .ad-skyscraper .cta { left: 43px; top: 761px; width: 186px; height: 57px; font-size: 18px; }
</style>
</head>
<body>

  <section class="ad ad-leaderboard">
    <svg class="ad-art" viewBox="0 0 1037 129" preserveAspectRatio="none">
      <defs>
        <linearGradient id="paper-leaderboard" x1="0" y1="0" x2="1" y2="1">
          <stop offset="0" stop-color="var(--photo-mid)"/>
          <stop offset="0.5" stop-color="var(--photo-light)"/>
          <stop offset="1" stop-color="var(--photo-warm)"/>
        </linearGradient>
      </defs>
      <polygon role="img" aria-label="Photo of a hand flipping through a stack of tabbed office papers" points="680,0 1037,0 1037,129 585,129" fill="url(#paper-leaderboard)"/>
      <polygon points="104,0 637,0 541,129 0,129 0,72" fill="var(--brand-blue)"/>
    </svg>
    <div class="brand-name">Oak Ferry</div>
    <div class="copy">
      <h2 class="headline">Affordable On-Site Shredding</h2>
      <p class="description">Certified, Affordable Office Shredding Since 2003.<br>Fast, no contact shredding service.</p>
    </div>
    <div class="cta">Get a Quote</div>
  </section>

  <section class="ad ad-medium">
    <svg class="ad-art" viewBox="0 0 429 357" preserveAspectRatio="none">
      <defs>
        <linearGradient id="paper-medium" x1="0" y1="0" x2="1" y2="1">
          <stop offset="0" stop-color="var(--photo-warm)"/>
          <stop offset="0.45" stop-color="var(--photo-light)"/>
          <stop offset="1" stop-color="var(--photo-mid)"/>
        </linearGradient>
      </defs>
      <polygon role="img" aria-label="Photo of a hand flipping through a stack of tabbed office papers" points="190,0 429,0 429,230 0,140 0,132" fill="url(#paper-medium)"/>
      <polygon points="0,132 429,216 283,357 0,357" fill="var(--brand-blue)"/>
    </svg>
    <div class="brand-name">Oak Ferry</div>
    <div class="copy">
      <h2 class="headline">Affordable<br>On-Site Shredding</h2>
      <p class="description">Certified, Affordable Office Shredding Since 2003.<br>Fast, no contact shredding service.</p>
    </div>
    <div class="cta">Get a Quote</div>
  </section>

  <section class="ad ad-large">
    <svg class="ad-art" viewBox="0 0 481 400" preserveAspectRatio="none">
      <defs>
        <linearGradient id="paper-large" x1="0" y1="0" x2="1" y2="1">
          <stop offset="0" stop-color="var(--photo-warm)"/>
          <stop offset="0.45" stop-color="var(--photo-light)"/>
          <stop offset="1" stop-color="var(--photo-mid)"/>
        </linearGradient>
      </defs>
      <polygon role="img" aria-label="Photo of a hand flipping through a stack of tabbed office papers" points="175,0 481,0 481,270 0,185 0,178" fill="url(#paper-large)"/>
      <polygon points="0,178 481,262 481,282 393,400 0,400" fill="var(--brand-blue)"/>
    </svg>
    <div class="brand-name">Oak Ferry</div>
    <div class="copy">
      <h2 class="headline">Affordable<br>On-Site Shredding</h2>
      <p class="description">Certified, Affordable Office Shredding Since 2003.<br>Fast, no contact shredding service.</p>
    </div>
    <div class="cta">Get a Quote</div>
  </section>

  <section class="ad ad-skyscraper">
    <svg class="ad-art" viewBox="0 0 430 857" preserveAspectRatio="none">
      <defs>
        <linearGradient id="paper-skyscraper" x1="0" y1="0" x2="0.6" y2="1">
          <stop offset="0" stop-color="var(--photo-warm)"/>
          <stop offset="0.35" stop-color="var(--photo-light)"/>
          <stop offset="1" stop-color="var(--photo-mid)"/>
        </linearGradient>
      </defs>
      <polygon role="img" aria-label="Photo of a hand flipping through a tall stack of tabbed office papers" points="115,0 430,0 430,545 0,430 0,165" fill="url(#paper-skyscraper)"/>
      <polygon points="0,424 430,535 430,736 345,857 0,857" fill="var(--brand-blue)"/>
    </svg>
    <div class="brand-name">Oak Ferry</div>
    <div class="copy">
      <h2 class="headline">Affordable<br>On-Site Shredding</h2>
      <p class="description">Certified, Affordable Office Shredding Since 2003.<br>Fast, no contact shredding service.</p>
    </div>
    <div class="cta">Get a Quote</div>
  </section>

</body>
</html>
```